Promotional Flyer for "Ventaro events" with LOGO DESIGN

I am developing my own start-up company which is organising and managing exclusive and luxury events in Vienna, London, and Venice. Elegant promotional flyer should introduce and promote my company to a broad spectrum of high level clients; both online and by regular hardcopy post. This flyer should reflect the highest level of elegance, professionalism, creativity, sophistication, and exclusivity as well as irradiating a feeling of child like joy . I want the flyer to be two sided or folded, but did not find that version. It should be including the photo from the main page of the site "www.ventaro-events.example". Text should contain the following :
Creative ideas and event concept
Unique venue selection
Complete planning and coordination
First class catering
Professional photography and video productions ---
--------------------------------------------------------------------
1.Surprise the unsurprisable
2. we materialise your innermost dreams into trend setting entertainment and unique celebration of any occasion
------------------------------------------------------------------------
You can take ideas from any photo on my website, I also add some additional photos
I am available via e-mail or phone +390000000000 /+440000000000. Thank you.

Target Market(s)

high level discreet and the discerning client with taste, well travelled already spoiled

Industry/Entity Type

Event Planning

Font styles to use
Sans Serif

Colors
ffffff
fffbf0

Requirements
Must have
• unexpected simlicity, be extremely different from all what is there on the market
Should not have
• eye catching and memorable yet not too busy

```html
<!DOCTYPE html>
<html lang="en">
<head>
<meta charset="utf-8">
<title>Ventaro events – Flyer</title>
<link href="https://fonts.googleapis.com/css2?family=Open+Sans:wght@300;400;700&display=swap" rel="stylesheet">
<style>
  :root {
    --paper: #ffffff;
    --panel: #333132;
    --band: #050404;
    --gold: #f5b82e;
    --ink: #ffffff;
    --ink-soft: #e8e6e3;
    --photo-hall: #8a6a3a;
    --photo-wings: #5b4a7c;
    --photo-gowns: #7a4a34;
  }
  * { box-sizing: border-box; margin: 0; padding: 0; }
  html, body {
    width: 1200px; height: 869px; overflow: hidden;
    background: var(--paper);
    font-family: "Open Sans", Arial, sans-serif;
  }
  .flyer {
    position: absolute; left: 12px; top: 12px;
    width: 1176px; height: 845px;
    background: var(--band);
    overflow: hidden;
  }
  .info-panel {
    position: absolute; left: 0; top: 0;
    width: 823px; height: 606px;
    background: var(--panel);
  }
  .headline {
    position: absolute; left: 118px; top: 88px;
    font-weight: 300; font-size: 44px; color: var(--gold);
    letter-spacing: 0.2px; white-space: nowrap;
  }
  .intro {
    position: absolute; left: 118px; top: 150px;
    font-weight: 300; font-size: 22.5px; line-height: 30px; color: var(--ink);
  }
  .services {
    position: absolute; left: 118px; top: 227px;
    list-style: none;
  }
  .services li {
    position: relative; padding-left: 24px;
    font-weight: 300; font-size: 22.5px; line-height: 37.5px; color: var(--ink);
    white-space: nowrap;
  }
  .services li::before {
    content: ""; position: absolute; left: 0; top: 12px;
    width: 13px; height: 13px; border: 2px solid var(--gold); border-radius: 50%;
  }
  .contacts {
    position: absolute; left: 118px; top: 429px;
    font-size: 22.5px; line-height: 38.5px; color: var(--ink);
  }
  .contacts dt { display: inline; font-weight: 700; color: var(--gold); }
  .contacts dd { display: inline; font-weight: 400; }
  .contacts div { white-space: nowrap; }
  .photo-column {
    position: absolute; left: 823px; top: 0;
    width: 353px; height: 606px;
  }
  .photo { position: absolute; left: 0; width: 353px; }
  .photo--hall {
    top: 0; height: 220px;
    background: radial-gradient(ellipse at 40% 30%, #e2c27a 0%, var(--photo-hall) 45%, #3a2614 100%);
  }
  .photo--wings {
    top: 222px; height: 191px;
    background: radial-gradient(ellipse at 50% 45%, #b7a3d8 0%, var(--photo-wings) 40%, #1e1a3a 100%);
  }
  .photo--gowns {
    top: 415px; height: 191px;
    background: radial-gradient(ellipse at 50% 55%, #e6c2a6 0%, var(--photo-gowns) 45%, #1c0f0a 100%);
  }
  .brand-band {
    position: absolute; left: 0; top: 606px;
    width: 1176px; height: 239px;
    background:
      radial-gradient(circle at 60px 40px, rgba(245,184,46,0.35) 0, rgba(245,184,46,0) 28px),
      radial-gradient(circle at 95px 150px, rgba(245,184,46,0.3) 0, rgba(245,184,46,0) 22px),
      radial-gradient(circle at 520px 20px, rgba(245,184,46,0.25) 0, rgba(245,184,46,0) 10px),
      radial-gradient(ellipse at 70% 80%, #140a06 0%, var(--band) 60%);
  }
  .brand-name {
    position: absolute; left: 118px; top: 78px;
    font-weight: 400; font-size: 44px; color: var(--gold);
    white-space: nowrap;
  }
  .tagline {
    position: absolute; left: 475px; top: 93px;
    font-weight: 300; font-size: 22px; letter-spacing: 2.2px; color: var(--ink-soft);
    white-space: nowrap;
  }
</style>
</head>
<body>
  <main class="flyer">
    <section class="info-panel">
      <h1 class="headline">Surprise the unsurprisable</h1>
      <p class="intro">We materialise your innermost dreams into trend setting<br>entertainment and unique celebration of any occasion.</p>
      <ul class="services">
        <li>Creative ideas and event concept</li>
        <li>Unique venue selection</li>
        <li>Complete planning and coordination</li>
        <li>First class catering</li>
        <li>Professional photography and video productions</li>
      </ul>
      <dl class="contacts">
        <div><dt>Locations:</dt> <dd>Venice / London / Vienna / Moscow</dd></div>
        <div><dt>Call:</dt> <dd>+390 000 000 000 / +440 000 000 000 / +440 000 000 001</dd></div>
        <div><dt>Email:</dt> <dd>marketing@ventaro-events.example</dd></div>
        <div><dt>Website:</dt> <dd>www.ventaro-events.example</dd></div>
      </dl>
    </section>
    <aside class="photo-column">
      <div class="photo photo--hall" role="img" aria-label="Guests mingling in an ornate gilded ballroom lit by crystal chandeliers"></div>
      <div class="photo photo--wings" role="img" aria-label="Performer in a shimmering violet winged costume on a stage in blue light"></div>
      <div class="photo photo--gowns" role="img" aria-label="Three singers in baroque gowns and powdered wigs performing at an evening event"></div>
    </aside>
    <footer class="brand-band">
      <div class="brand-name">Ventaro events</div>
      <p class="tagline">EXCLUSIVE / EXTRAORDINARY / EXOTIC</p>
    </footer>
  </main>
</body>
</html>
```